CoreVANTX Web Design Project

We would like a website design to go with the new logo. They want something to model this site: http://www.halbrenquist.example
Using the blue (#3366FF) and green (#33CC33). Like the bight colors in the top half of the home page. Must have a mini form on the interior pages.
Also like this site for inspiration:
http://www.davrelpointgroup.example/
Industry/Entity Type
Interior
Requirements
Must have
- Must fit the brief you had from before.
Must have a mini form
Should not have
- Doesn't have to have to pop up navigation over the slider on the home page.

```html
<!DOCTYPE html>
<html lang="en">
<head>
<meta charset="utf-8">
<title>CoreVANTX — Communicating</title>
<link href="https://fonts.googleapis.com/css2?family=Montserrat:wght@400;500;600;700&family=Arimo:wght@400;700&family=Gochi+Hand&display=swap" rel="stylesheet">
<style>
  :root {
    --blue: #3366ff;
    --blue-light: #86a6ff;
    --green: #33cc33;
    --green-bright: #22e011;
    --green-deep: #0aa80a;
    --grey-text: #666666;
    --grey-dark: #333333;
    --white: #ffffff;
    --caption-bg: rgba(40, 40, 40, 0.72);
  }
  html, body { margin: 0; padding: 0; overflow: hidden; background: var(--white); }
  .canvas {
    position: relative;
    width: 1108px;
    height: 1200px;
    overflow: hidden;
    background: linear-gradient(#f1f1f1 0, #ffffff 150px, #ffffff 330px);
    font-family: "Arimo", Arial, sans-serif;
  }
  .abs { position: absolute; }

  .brand {
    left: 71px; top: 30px;
    font-family: "Montserrat", sans-serif;
    font-weight: 500;
    font-size: 62px;
    letter-spacing: -2px;
    color: var(--grey-text);
    line-height: 1;
  }

  .main-nav { left: 71px; top: 131px; margin: 0; padding: 0; list-style: none; }
  .main-nav li {
    position: absolute; top: 0; white-space: nowrap;
    font-family: "Montserrat", sans-serif; font-weight: 600;
    font-size: 16.5px; color: var(--blue); letter-spacing: 0.3px;
  }

  .headline {
    left: 70px; top: 168px; margin: 0;
    font-family: "Gochi Hand", cursive;
    font-weight: 400; font-size: 112px; line-height: 1;
    color: var(--green); letter-spacing: 1px;
  }
  .tagline {
    left: 75px; top: 288px; margin: 0;
    font-family: "Arimo", Arial, sans-serif; font-weight: 700;
    font-size: 19.5px; color: var(--grey-text);
  }

  .band { left: 0; top: 330px; }

  .quote-panel {
    left: 688px; top: 328px; width: 352px; height: 380px;
    background: var(--blue); border-radius: 5px 5px 0 0;
  }
  .quote-title {
    left: 31px; top: 22px; margin: 0;
    font-family: "Montserrat", sans-serif; font-weight: 700;
    font-size: 16px; color: var(--white); letter-spacing: 0.3px;
  }
  .field {
    left: 30px; width: 303px; height: 37px;
    border: 3px solid var(--blue-light); border-radius: 4px;
    background: var(--white);
    font-family: "Montserrat", sans-serif; font-size: 16.5px; color: #555;
  }
  .field svg { position: absolute; left: 9px; top: 8px; }
  .field span { position: absolute; left: 38px; top: 8px; }
  .field .select-btn {
    position: absolute; right: 0; top: 0; width: 37px; height: 37px;
    background: linear-gradient(#5a5a5a, #2c2c2c); border-radius: 0 2px 2px 0;
  }
  .quote-button {
    left: 30px; top: 304px; width: 312px; height: 40px;
    background: linear-gradient(var(--green-bright), var(--green-deep));
    border-radius: 3px; box-shadow: 0 3px 0 #1b5e1b;
    color: var(--white); text-align: center; line-height: 40px;
    font-family: "Montserrat", sans-serif; font-weight: 700; font-size: 16px; letter-spacing: 0.5px;
  }

  .intro {
    left: 69px; top: 405px; width: 618px;
    color: var(--white); font-size: 16.3px; line-height: 20px;
  }
  .intro p { margin: 0 0 20px; }

  .card { top: 726px; width: 307px; }
  .card-media { position: relative; width: 307px; height: 205px; }
  .card-caption {
    position: absolute; left: 0; bottom: 0; width: 100%; height: 44px;
    background: var(--caption-bg); color: var(--white);
    font-family: "Montserrat", sans-serif; font-weight: 500; font-size: 23.5px;
    line-height: 44px; padding-left: 15px; box-sizing: border-box;
  }
  .card-text {
    margin: 13px 0 0; color: var(--white);
    font-size: 16.3px; line-height: 20px;
  }
  .read-more {
    margin-top: 14px; color: var(--white);
    font-family: "Montserrat", sans-serif; font-weight: 700; font-size: 12.5px; letter-spacing: 0.5px;
  }

  .footer {
    left: 0; top: 1122px; width: 1108px; height: 78px;
    background: linear-gradient(#ececec, #ffffff);
  }
  .legal {
    left: 70px; top: 24px; margin: 0;
    font-family: "Montserrat", sans-serif; font-size: 12.8px; color: var(--grey-dark); letter-spacing: 0.3px;
  }
  .legal a { color: var(--blue); text-decoration: none; }
  .footer-brand {
    left: 858px; top: 22px;
    font-family: "Montserrat", sans-serif; font-weight: 500;
    font-size: 28px; letter-spacing: -1px; color: var(--grey-text); line-height: 1;
  }
</style>
</head>
<body>
<div class="canvas">

  <div class="abs brand">CoreVANTX</div>

  <ul class="abs main-nav">
    <li style="left:0">WHO WE ARE</li>
    <li style="left:147px">WHAT WE DO</li>
    <li style="left:294px">COMMUNITY</li>
    <li style="left:428px">CAREERS</li>
    <li style="left:535px">CONTACT</li>
  </ul>

  <h1 class="abs headline">Communicating</h1>
  <p class="abs tagline">Enterprise Technology clients.</p>

  <svg class="abs band" width="1108" height="792" viewBox="0 0 1108 792" aria-hidden="true">
    <polygon points="0,27 1108,13 1108,792 0,792" fill="var(--green)"/>
    <polygon points="0,58 1108,26 1108,792 0,792" fill="var(--blue)"/>
  </svg>

  <div class="abs quote-panel">
    <h2 class="abs quote-title">FREE QUOTE</h2>

    <div class="abs field" style="top:71px">
      <svg width="20" height="20" viewBox="0 0 20 20" aria-hidden="true"><circle cx="10" cy="6" r="4.5" fill="#aaa"/><path d="M1 20c0-6 4-9 9-9s9 3 9 9z" fill="#aaa"/></svg>
      <span>name</span>
    </div>
    <div class="abs field" style="top:127px">
      <svg width="20" height="20" viewBox="0 0 20 20" aria-hidden="true"><path d="M4 1l4 4-2 3c1 2 3 4 5 5l3-2 4 4-3 3C8 18 2 12 1 4z" fill="#aaa"/></svg>
      <span>telephone</span>
    </div>
    <div class="abs field" style="top:184px">
      <svg width="20" height="20" viewBox="0 0 20 20" aria-hidden="true"><rect x="1" y="4" width="18" height="12" fill="#aaa"/><path d="M1 4l9 7 9-7" stroke="#fff" stroke-width="1.5" fill="none"/></svg>
      <span>email</span>
    </div>
    <div class="abs field" style="top:240px">
      <svg width="20" height="20" viewBox="0 0 20 20" aria-hidden="true"><path d="M11 1l8 8-3 1-3 3v4l-2 1-4-4-5 5-1-1 5-5-4-4 1-2h4l3-3z" fill="#aaa"/></svg>
      <span>interested in</span>
      <div class="select-btn">
        <svg width="37" height="37" viewBox="0 0 37 37" aria-hidden="true" style="left:0;top:0"><path d="M14 16l4.5-5 4.5 5z M14 21l4.5 5 4.5-5z" fill="#fff"/></svg>
      </div>
    </div>

    <div class="abs quote-button">GET A FREE QUOTE</div>
  </div>

  <div class="abs intro">
    <p>Lorem ipsum dolor sit amet, consectetur adipiscing elit. Nunc eu massa sem, venenatis adipiscing nulla. Sed tempor posuere orci sit amet gravida. Aenean nisi augue, bibendum in ornare eget, volutpat porta sapien. Suspendisse viverra sagittis arcu, euismod luctus dui euismod sed. Aenean tincidunt, justo blandit interdum tincidunt, erat odio sagittis orci, pulvinar ullamcorper neque diam volutpat augue. Suspendisse at lobortis felis. Nunc aliquam risus quis augue gravida porta.</p>
    <p>Morbi vel nibh ut leo ullamcorper hendrerit sed id augue. Aenean non leo justo. Cum sociis natoque penatibus et magnis dis parturient montes, nascetur ridiculus mus. Maecenas erat tellus, pretium consectetur semper ut, placerat nec velit. Morbi luctus fermentum libero eu gravida. Quisque sodales erat non urna sodales convallis sit amet vitae leo. Ut et elit ac arcu convallis vestibulum non non ligulln ultrices lacus condimentum.</p>
  </div>

  <div class="abs card" style="left:72px">
    <div class="card-media" role="img" aria-label="Photo: colleagues at a desk reviewing documents beside a laptop" style="background:linear-gradient(135deg,#e6ecf3,#b9c6d6 60%,#8796aa)">
      <div class="card-caption">Heading One</div>
    </div>
    <p class="card-text">Lorem ipsium dolor sit amet, consect etur adipiscloing elit. Nunc eu massa sem, venenatis adipiscing nulla. Sed tempor posulore iere orci sit amet gra vida. Aenean nisi augue, biben dum.</p>
    <div class="read-more">+ READ MORE</div>
  </div>

  <div class="abs card" style="left:400px">
    <div class="card-media" role="img" aria-label="Photo: smiling young businessman giving a thumbs up in a bright office" style="background:linear-gradient(160deg,#f2f4f6,#d6dde4 55%,#a9b4c0)">
      <div class="card-caption">Heading Two</div>
    </div>
    <p class="card-text">Lorem ipsium dolor sit amet, consect etur adipiscloing elit. Nunc eu massa sem, venenatis adipiscing nulla. Sed tempor posulore iere orci sit amet gra vida. Aenean nisdum in ornare eget.</p>
    <div class="read-more">+ READ MORE</div>
  </div>

  <div class="abs card" style="left:729px">
    <div class="card-media" role="img" aria-label="Photo: three business people meeting around a laptop" style="background:linear-gradient(150deg,#eef1f4,#c9d0d8 50%,#5a6270)">
      <div class="card-caption">Heading Three</div>
    </div>
    <p class="card-text">Lorem ipsium dolor sit amet, consect etur adipiscloing elit. Nunc eu massa sem, venenatis adipiscing nulla. Sed tempor posulore ieregue, biben dum in ornare eget.</p>
    <div class="read-more">+ READ MORE</div>
  </div>

  <footer class="abs footer">
    <p class="abs legal">COPYRIGHT © 2012 COREVANTX. ALL RIGHTS RESERVED. &nbsp;|&nbsp; <a href="#">TERMS OF USE</a></p>
    <div class="abs footer-brand">CoreVANTX</div>
  </footer>

</div>
</body>
</html>
```